Quorvex business card design

create modern and tech looking business card that is clean but effectively communciates that we are a cloud communications company.
Should have at minimum:
Employee Name
Postion
Phone Number
Email
website
create modern and tech looking business card that is clean but effectively communciates that we are a cloud communications company. We have two logo color schemes (attached) so would like to see designs both ways
Should have at minimum:
Employee Name
Postion
Phone Number
Email
website

```html
<!DOCTYPE html>
<html lang="en">
<head>
<meta charset="utf-8">
<title>Quorvex business card</title>
<link rel="stylesheet" href="https://fonts.googleapis.com/css2?family=Exo+2:wght@500;600&family=Lato:wght@400;700;900&display=swap">
<style>
  :root {
    --stage: #ececec;
    --card-dark: #050505;
    --card-light: #f5f5f5;
    --panel: #e6e6e6;
    --lime: #8dc63f;
    --ink: #3a3a3a;
    --ink-soft: #5a5a5a;
    --wordmark-dark: #555555;
  }
  * { box-sizing: border-box; margin: 0; padding: 0; }
  html, body { width: 1200px; height: 750px; overflow: hidden; }
  body {
    background: var(--stage);
    position: relative;
    font-family: "Lato", sans-serif;
  }
  .card {
    position: absolute;
    width: 525px;
    height: 300px;
    border-radius: 28px;
    overflow: hidden;
    box-shadow: 0 10px 30px rgba(0,0,0,0.18);
  }
  .card-front { left: 60px; top: 80px; background: var(--card-dark); }
  .card-back { left: 615px; top: 370px; background: var(--card-light); }

  .brand {
    position: absolute;
    display: flex;
    align-items: center;
    gap: 14px;
  }
  .brand-mark { width: 26px; height: 26px; background: var(--lime); }
  .brand-name {
    font-family: "Exo 2", sans-serif;
    font-weight: 600;
    font-size: 52px;
    letter-spacing: 3px;
    text-transform: uppercase;
  }
  .card-front .brand { left: 120px; top: 112px; }
  .card-front .brand-name { color: var(--wordmark-dark); }
  .card-back .brand { left: 48px; top: 124px; }
  .card-back .brand-mark { width: 20px; height: 20px; }
  .card-back .brand-name { color: var(--ink); font-size: 38px; letter-spacing: 2px; }

  .edge-band {
    position: absolute; left: 0; top: 0; bottom: 0;
    width: 16px; background: var(--lime);
  }
  .edge-rule {
    position: absolute; right: 22px; top: 22px; bottom: 22px;
    width: 5px; background: var(--lime);
  }
  .info-panel {
    position: absolute; left: 300px; top: 22px; bottom: 22px; right: 40px;
    background: var(--panel);
    padding: 26px 18px 0 22px;
    color: var(--ink);
  }
  .tag {
    display: inline-block;
    background: var(--lime);
    color: #fff;
    font-weight: 900;
    font-size: 11px;
    padding: 3px 7px;
    letter-spacing: 0.3px;
  }
  .person-name { font-size: 19px; margin-top: 4px; line-height: 1.1; }
  .person-name .first { font-weight: 900; }
  .person-name .last { font-weight: 400; }
  .person-role { font-size: 11.5px; color: var(--ink-soft); margin-bottom: 20px; }
  .contact { font-size: 11.5px; line-height: 1.45; color: var(--ink); }
  .contact-address { margin: 6px 0 14px; }
</style>
</head>
<body>
  <section class="card card-front" aria-label="Card front">
    <div class="brand">
      <span class="brand-mark"></span>
      <span class="brand-name">Quorvex</span>
    </div>
  </section>

  <section class="card card-back" aria-label="Card back">
    <span class="edge-band"></span>
    <div class="brand">
      <span class="brand-mark"></span>
      <span class="brand-name">Quorvex</span>
    </div>
    <div class="info-panel">
      <span class="tag">Hello!</span>
      <p class="person-name"><span class="first">DARA</span> <span class="last">OLSEN</span></p>
      <p class="person-role">Graphic Designer</p>
      <span class="tag">Get in touch</span>
      <p class="contact contact-address">42 Larkfield Avenue<br>Oregon OR 97201</p>
      <p class="contact">000 . 1234 . 5678<br>mymail@email.com<br>www.website.com</p>
    </div>
    <span class="edge-rule"></span>
  </section>
</body>
</html>
```